Anzeigengestaltung für Anwalt
Zielgruppe
Ich: Anwalt im Bereich Patente, Marken, etc.
Zielgruppe: Britische Anwälte/Kanzleien mit gleichem Schwerpunkt
Aufgabenstellung
Projektbeschreibung:
Anzeige für ein britisches Magazin; Beispiel hier https://folvra.com/hxta-bulletin/docs/hxta-2017-05-may-2017?e=61490358/73920415 z.B. Seite 80
Größe: 90mm breit x 112mm tief
Farben und Logo „Velorin“ sollen sich an meiner HP www.velorin.de orientieren
Hintergrund für den Text: stilisierte Karten von Großbritannien und Kontinentaleuropa, verbunden mit einer Brücke
Anzeigentext in beigefügter Datei.

```html
<!DOCTYPE html>
<html lang="en">
<head>
<meta charset="utf-8">
<title>Velorin – Develop your footprint in continental Europe</title>
<link rel="stylesheet" href="https://fonts.googleapis.com/css2?family=EB+Garamond:ital,wght@0,400;0,500;0,600;1,400&display=swap">
<style>
  :root {
    --ink: #1c1f26;
    --brand-blue: #2f5fae;
    --band-blue: #3563b5;
    --paper: #ffffff;
    --map-light: #eef1f5;
    --map-mid: #c9d1dc;
    --frame: #9aa3ae;
  }
  * { margin: 0; padding: 0; box-sizing: border-box; }
  html, body {
    width: 932px; height: 1200px; overflow: hidden;
    background: var(--paper);
    font-family: "EB Garamond", "Times New Roman", serif;
    color: var(--ink);
  }
  .ad {
    position: relative;
    width: 932px; height: 1200px;
    border: 3px solid var(--frame);
    background: var(--paper);
    overflow: hidden;
  }
  .map-backdrop {
    position: absolute; left: 0; top: 0; width: 100%; height: 640px;
    background: radial-gradient(ellipse at 65% 45%, var(--map-mid) 0%, var(--map-light) 55%, var(--paper) 100%);
  }
  .brand {
    position: absolute; left: 50px; top: 40px;
    display: flex; align-items: baseline; gap: 34px;
    color: var(--brand-blue);
  }
  .brand-name { font-size: 64px; font-weight: 500; }
  .brand-tagline { font-size: 34px; font-style: italic; }
  .headline {
    position: absolute; left: 70px; top: 200px;
    font-size: 46px; font-variant: small-caps; letter-spacing: 2px; line-height: 1.15;
    font-weight: 500;
  }
  .headline span { display: block; padding-left: 0; }
  .headline span + span { padding-left: 0; }
  .copy {
    position: absolute; left: 70px; top: 360px; right: 60px;
    font-size: 33px; line-height: 1.22;
  }
  .copy .lead { color: var(--brand-blue); margin-top: 22px; }
  .copy .lead:first-child { margin-top: 0; }
  .copy ul { list-style: none; }
  .copy ul.bullets li::before { content: "• "; }
  .contact-band {
    position: absolute; left: 0; right: 0; top: 1020px; height: 70px;
    background: var(--band-blue); color: var(--paper);
    font-size: 34px; display: flex; align-items: center; padding-left: 70px;
  }
  .signoff {
    position: absolute; left: 70px; top: 1110px;
    font-size: 34px; font-style: italic; color: var(--brand-blue);
  }
</style>
</head>
<body>
  <div class="ad">
    <div class="map-backdrop" role="img" aria-label="Stylised maps of Great Britain and continental Europe joined by a bridge"></div>

    <div class="brand">
      <span class="brand-name">Velorin</span>
      <span class="brand-tagline">Your bridge to the continent</span>
    </div>

    <h1 class="headline">
      <span>Develop your footprint</span>
      <span>in continental Europe</span>
    </h1>

    <div class="copy">
      <p class="lead">Velorin could be</p>
      <ul>
        <li>A possible gateway to the EU, to Germany, to Munich</li>
        <li>A starting point for a roadmap to your EU desk</li>
        <li>Your door to your new Munich office</li>
        <li>A part-time solution</li>
      </ul>
      <p class="lead">Services offered to start a co-operation</p>
      <ul>
        <li>White label services</li>
        <li>Oral proceedings deputy in Munich</li>
        <li>Work sample offered free of charge</li>
      </ul>
      <ul class="bullets">
        <li>Significant experiences with</li>
        <li>Oppositions, Appeals and Infringement cases</li>
        <li>Background in Chemistry – from APIs to zeolites</li>
      </ul>
    </div>

    <div class="contact-band">Contact Anselm Reutter at mail@velorin.com</div>
    <p class="signoff">Velorin - stay in touch with the continent</p>
  </div>
</body>
</html>
```